Flyer für eine Zahnarztpraxis
Zielgruppe
Zahnarztpraxis, Zielgruppe sind Patienten im Erwachsenenalter
Aufgabenstellung
Den Text habe ich bereits geschrieben. Es soll ein DINA4 Flyer werden, mit sechs Seiten.

```html
<!DOCTYPE html>
<html lang="de">
<head>
<meta charset="utf-8">
<title>Flyer Vitamin D – Zahnarztpraxis Lindenhof</title>
<link rel="stylesheet" href="https://fonts.googleapis.com/css2?family=Barlow:wght@300;400;500&family=Barlow+Semi+Condensed:wght@400;500&family=Dancing+Script:wght@500&display=swap">
<style>
  :root {
    --bg: #e6e7e8;
    --paper: #ffffff;
    --teal: #2e6a5c;
    --teal-soft: #4d7d71;
    --orange: #e3a035;
    --sun: #e8a93a;
    --yellow: #f1d34a;
    --photo-a: #f3c24a;
    --photo-b: #b86f1c;
    --photo-c: #5a3a12;
  }
  * { box-sizing: border-box; margin: 0; padding: 0; }
  html, body { width: 1200px; height: 547px; overflow: hidden; background: var(--bg); }
  body { position: relative; font-family: "Barlow Semi Condensed", sans-serif; color: var(--teal); }

  .spread {
    position: absolute; top: 136px; width: 580px; height: 274px;
    background: var(--paper); overflow: hidden;
    box-shadow: 0 4px 12px rgba(0,0,0,.18);
  }
  .spread--outside { left: 10px; }
  .spread--inside { left: 610px; }
  .abs { position: absolute; }

  .heading {
    font-family: "Barlow", sans-serif; font-weight: 300;
    font-size: 14.5px; line-height: 1.08; color: var(--teal); z-index: 2;
  }
  .body-tiny { font-size: 3.6px; line-height: 1.9; color: var(--teal-soft); z-index: 2; }
  .lead { font-family: "Barlow", sans-serif; font-weight: 300; font-size: 8.6px; line-height: 1.22; z-index: 2; }
  .script { font-family: "Dancing Script", cursive; color: var(--orange); font-size: 6.4px; line-height: 1.45; transform: rotate(-4deg); }

  .bullets { list-style: none; }
  .bullets li { position: relative; padding-left: 12px; margin-bottom: 5px; }
  .bullets li::before {
    content: ""; position: absolute; left: 0; top: 1px; width: 7px; height: 3px;
    background: var(--orange); clip-path: polygon(0 25%,60% 25%,60% 0,100% 50%,60% 100%,60% 75%,0 75%);
  }

  .sun { position: absolute; }
  .phone { display: flex; align-items: center; gap: 4px; font-size: 5px; font-weight: 500; color: var(--teal); }
  .phone-icon { width: 9px; height: 9px; border-radius: 50%; background: var(--yellow); display: grid; place-items: center; }

  .brand { display: flex; align-items: center; gap: 4px; font-family: "Barlow", sans-serif; font-size: 3.6px; line-height: 1.25; color: var(--teal); letter-spacing: .03em; }
  .brand-mark { width: 9px; height: 9px; border-radius: 50%; border: 0.8px solid var(--teal); }

  .cover-title { font-family: "Barlow", sans-serif; font-weight: 300; font-size: 15px; color: var(--teal); white-space: nowrap; }
  .cover-title small { font-size: 8px; }
  .cover-sub { font-family: "Barlow", sans-serif; font-weight: 400; font-size: 7.4px; color: var(--teal-soft); }
  .pill { display: inline-block; background: var(--yellow); border-radius: 3px; padding: 1px 4px; font-size: 3px; color: var(--teal); }

  .portrait { z-index: 1; }
  .checks { list-style: none; }
  .checks li { display: flex; align-items: center; gap: 5px; margin-bottom: 4.2px; }
  .check-icon { width: 5px; height: 5px; flex: none; }
</style>
</head>
<body>

<section class="spread spread--outside" aria-label="Flyer Außenseite">

  <h2 class="heading abs" style="left:70px;top:64px;">Kennen Sie diese<br>Situationen?</h2>
  <ul class="bullets body-tiny abs" style="left:58px;top:120px;width:125px;">
    <li>Sie kommen selten an die frische Luft, besonders im Winter?</li>
    <li>Sie haben schon einmal von Ihrem Arzt gehört, dass Ihr Vitamin-D-Wert niedrig ist?</li>
    <li>Ihr Zahnfleisch ist empfindlich oder Sie hatten schon Zahnverlust?<br>Dann könnte es sinnvoll sein, Ihren Vitamin-D-Status zu besprechen.<br>Fragen Sie uns – wir helfen Ihnen gern weiter.</li>
  </ul>

  <p class="body-tiny abs" style="left:204px;top:122px;width:44px;">Unser Praxisteam berät Sie gern persönlich und beantwortet Ihre Fragen.</p>

  <svg class="sun" style="left:150px;top:210px;" width="86" height="64" viewBox="0 0 86 64" role="img" aria-label="Sonnen-Ornament">
    <circle cx="43" cy="64" r="42" fill="var(--yellow)" opacity=".55"/>
    <circle cx="43" cy="64" r="24" fill="var(--sun)"/>
  </svg>

  <h2 class="heading abs" style="left:263px;top:64px;">Ihr Lächeln und<br>Ihre Gesundheit<br>sind es wert!</h2>
  <p class="lead abs" style="left:263px;top:119px;width:110px;color:var(--teal-soft);">Vitamin D ist ein wichti-<br>ger Baustein für ein ge-<br>sundes Leben – und ge-<br>sunde Zähne.</p>

  <p class="script abs" style="left:316px;top:186px;">Kommen Sie einfach<br>&nbsp;&nbsp;&nbsp;auf uns zu –<br>für Ihre Gesundheit von<br>Kopf bis Fuß.</p>

  <div class="phone abs" style="left:306px;top:252px;">
    <span class="phone-icon"><svg width="5" height="5" viewBox="0 0 24 24"><path fill="var(--teal)" d="M6.6 10.8a15 15 0 0 0 6.6 6.6l2.2-2.2c.3-.3.7-.4 1-.2 1.1.4 2.3.6 3.6.6.6 0 1 .4 1 1V20c0 .6-.4 1-1 1A17 17 0 0 1 3 4c0-.6.4-1 1-1h3.5c.6 0 1 .4 1 1 0 1.3.2 2.5.6 3.6.1.3 0 .7-.2 1z"/></svg></span>
    05123-48890
  </div>

  <svg class="abs" style="left:400px;top:0;" width="180" height="180" viewBox="0 0 180 180" role="img" aria-label="Foto: Frau genießt mit geschlossenen Augen die Sonne, daneben Vitamin-D-Kapseln">
    <defs>
      <linearGradient id="photoGlow" x1="1" y1="0" x2="0" y2="1">
        <stop offset="0" stop-color="var(--photo-a)"/>
        <stop offset=".55" stop-color="var(--photo-b)"/>
        <stop offset="1" stop-color="var(--photo-c)"/>
      </linearGradient>
    </defs>
    <path d="M84 0 H180 V180 H38 Q2 180 2 142 Q3 122 20 100 Z" fill="url(#photoGlow)" stroke="var(--sun)" stroke-width="1"/>
  </svg>

  <div class="brand abs" style="left:396px;top:13px;">
    <span class="brand-mark"></span>
    <span>ZAHNARZTPRAXIS<br>LINDENHOF &amp; TEAM</span>
  </div>

  <p class="cover-title abs" style="left:410px;top:193px;">Vitamin D – <small>mehr</small></p>
  <p class="cover-sub abs" style="left:410px;top:212px;">als nur Sonnenvitamin</p>
  <p class="body-tiny abs" style="left:410px;top:224px;font-size:4px;">Was Ihre Zähne und Ihr Körper jetzt brauchen könnten</p>
  <p class="body-tiny abs" style="left:410px;top:234px;width:120px;">Fühlen Sie sich oft müde? Haben Sie manchmal Zahnfleischprobleme oder empfindliche Zähne? Vielleicht steckt mehr dahinter, als Sie denken …</p>
  <span class="pill abs" style="left:410px;top:255px;">zahnarztpraxis-lindenhof.de</span>

  <svg class="sun" style="left:540px;top:232px;" width="40" height="42" viewBox="0 0 40 42" role="img" aria-label="Sonnen-Ornament">
    <circle cx="40" cy="42" r="38" fill="var(--yellow)" opacity=".55"/>
    <circle cx="40" cy="42" r="22" fill="var(--sun)"/>
  </svg>
</section>

<section class="spread spread--inside" aria-label="Flyer Innenseite">

  <h2 class="heading abs" style="left:28px;top:63px;">Was ist Vitamin D<br>eigentlich?</h2>
  <p class="body-tiny abs" style="left:28px;top:104px;width:125px;">Vitamin D wird oft „Sonnenvitamin“ genannt, weil unser Körper es größtenteils selbst bildet – wenn Sonne auf unsere Haut trifft. Doch in unseren Breitengraden reicht die Sonnenstrahlung viele Monate im Jahr nicht aus, um genügend Vitamin D zu bilden. Das Vitamin unterstützt nicht nur Knochen und Zähne, sondern auch unser Immunsystem, Muskeln und Wohlbefinden.</p>

  <svg class="abs" style="left:0;top:148px;" width="130" height="126" viewBox="0 0 130 126" role="img" aria-label="Illustration: Sonne mit Holzlöffel voller Vitamin-D-Kapseln">
    <defs>
      <radialGradient id="sunSpoon" cx=".65" cy=".45" r=".55">
        <stop offset="0" stop-color="var(--sun)"/>
        <stop offset=".6" stop-color="var(--yellow)"/>
        <stop offset="1" stop-color="var(--yellow)" stop-opacity="0"/>
      </radialGradient>
    </defs>
    <rect width="130" height="126" fill="url(#sunSpoon)"/>
  </svg>

  <div class="portrait abs" style="left:302px;top:62px;width:98px;height:212px;background:linear-gradient(180deg,#eae6dd,#cfd6dc);border-radius:44px 44px 0 0;" role="img" aria-label="Foto: lächelnde Frau mit erhobenem Daumen"></div>

  <h2 class="heading abs" style="left:204px;top:63px;">Warum ist<br>Vitamin D<br>so wichtig für<br>den Körper?</h2>
  <p class="body-tiny abs" style="left:204px;top:135px;width:82px;">Vitamin D wird oft „Sonnenvitamin“ genannt, weil unser Körper es größtenteils selbst bildet – wenn Sonne auf unsere Haut trifft. Doch in unseren Breitengraden reicht die Sonnenstrahlung viele Monate im Jahr nicht aus, um genügend Vitamin D zu bilden. Das Vitamin unterstützt nicht nur Knochen und Zähne, sondern auch unser Immunsystem, Muskeln und Wohlbefinden.</p>

  <h2 class="heading abs" style="left:410px;top:63px;">Vitamin D und Ihre<br>Zähne – eine starke<br>Verbindung</h2>
  <p class="body-tiny abs" style="left:422px;top:124px;width:122px;">Wussten Sie, dass Vitamin D entscheidend für gesunde Zähne ist? Es sorgt dafür, dass Kalzium im Körper optimal aufgenommen wird – und Kalzium ist der Baustoff für feste Zähne und stabilen Kieferknochen. Ein Mangel kann unter anderem begünstigen:</p>
  <ul class="checks body-tiny abs" style="left:414px;top:157px;width:132px;">
    <li><svg class="check-icon" viewBox="0 0 10 10"><circle cx="5" cy="5" r="5" fill="var(--teal)"/><path d="M2.8 5.2l1.5 1.5 3-3" stroke="#fff" stroke-width="1.2" fill="none"/></svg>Zahnfleischprobleme</li>
    <li><svg class="check-icon" viewBox="0 0 10 10"><circle cx="5" cy="5" r="5" fill="var(--teal)"/><path d="M2.8 5.2l1.5 1.5 3-3" stroke="#fff" stroke-width="1.2" fill="none"/></svg>Lockerung der Zähne</li>
    <li><svg class="check-icon" viewBox="0 0 10 10"><circle cx="5" cy="5" r="5" fill="var(--teal)"/><path d="M2.8 5.2l1.5 1.5 3-3" stroke="#fff" stroke-width="1.2" fill="none"/></svg>Schlechte Einheilung von Implantaten</li>
    <li><svg class="check-icon" viewBox="0 0 10 10"><circle cx="5" cy="5" r="5" fill="var(--teal)"/><path d="M2.8 5.2l1.5 1.5 3-3" stroke="#fff" stroke-width="1.2" fill="none"/></svg>Verzögerte Heilung nach zahnärztlichen Eingriffen</li>
  </ul>
  <p class="body-tiny abs" style="left:422px;top:200px;width:122px;">Gerade im Erwachsenenalter spielt Vitamin D eine wichtige Rolle, um den Zahnhalteapparat gesund zu halten.</p>

  <svg class="sun" style="left:540px;top:200px;" width="40" height="56" viewBox="0 0 40 56" role="img" aria-label="Sonnen-Ornament">
    <circle cx="40" cy="28" r="27" fill="var(--yellow)" opacity=".55"/>
    <circle cx="40" cy="28" r="15" fill="var(--sun)"/>
  </svg>
</section>

</body>
</html>
```